Firma für Temperaturmessung und Temperaturkalibrierung sucht Broschürendesign
Zielgruppe
Wir sind eine Firma für Temperaturmessung und Temperaturkalibrierung. Unsere Zielgruppe sind Unternehmen aus Industrie, Forschung & Entwicklung. Entsprechend suchen wir ein Design, das professionell unsere Produkte und Dienstleistungen repräsentiert.
Aufgabenstellung
Mögliche Maße sind:
DIN A6 = 10,5 x 14,8 cm
DIN B6 = 12,5 x 17,6 cm
DIN C6 = 11,4 x 16,2 cm
DIN D6 = 9,6 x 13,6 cm
Zur Orientierung des Designs sehen Sie folgende Webseiten:
https://www.vortilon.de/en/manufaktur/
https://www.vortilon.de/en/technologie/
Den Text sowie die Bilder, die zu verwenden sind, finden Sie in der unten stehenden Datei.

```html
<!DOCTYPE html>
<html lang="en">
<head>
<meta charset="utf-8">
<title>Vortilon Brochure – Precision Thermometers</title>
<link rel="stylesheet" href="https://fonts.googleapis.com/css2?family=Barlow:wght@300;400;600&display=swap">
<style>
  :root{
    --red:#d9261c;
    --red-dark:#b81d15;
    --ink:#3a3a3a;
    --muted:#9a9a9a;
    --paper:#ffffff;
    --stage:#e7e7e7;
    --shadow:rgba(0,0,0,.14);
  }
  *{box-sizing:border-box;margin:0;padding:0}
  html,body{width:1200px;height:2400px;overflow:hidden}
  body{background:var(--stage);font-family:"Barlow",Arial,sans-serif;color:var(--ink);position:relative}
  .spread{position:absolute;display:flex;box-shadow:0 8px 24px var(--shadow)}
  .page{position:relative;width:340px;height:480px;background:var(--paper);overflow:hidden}
  .spread .page + .page{border-left:1px solid #e4e4e4}
  .single{position:absolute;box-shadow:0 8px 24px var(--shadow)}
  .small .page{width:265px;height:375px}

  .brand{position:absolute;display:flex;align-items:center;gap:4px;font-weight:400;color:var(--ink);font-size:11px;letter-spacing:.5px}
  .brand::before{content:"";width:8px;height:8px;border-radius:50%;background:var(--red)}
  .brand.top{top:22px;right:24px}
  .brand.large{font-size:22px;gap:8px;top:38px;right:34px}
  .brand.large::before{width:15px;height:15px}

  .photo{position:absolute}
  .ph-lab{background:linear-gradient(135deg,#dfe3e8,#9aa3ad)}
  .ph-red{background:linear-gradient(135deg,#f1d3d1,#d9261c)}
  .ph-copper{background:linear-gradient(135deg,#d8d8d8,#b8734a 60%,#5a4036)}
  .ph-dark{background:linear-gradient(135deg,#5a5f66,#1f2226)}
  .ph-gold{background:linear-gradient(135deg,#c98f5b,#e8c23a 55%,#8a5a3a)}
  .ph-blue{background:linear-gradient(135deg,#e9ecf2,#4a64b8)}
  .ph-warm{background:linear-gradient(135deg,#f0e4d8,#b98a60)}
  .ph-person{background:linear-gradient(180deg,#d3d6da,#2b3344 60%,#8a2a22)}

  .h-red{color:var(--red);font-weight:600;font-size:7.5px;margin-bottom:3px}
  .body{font-size:6.6px;line-height:1.5;text-align:justify}
  .url{position:absolute;bottom:20px;font-size:6.5px;color:var(--red);letter-spacing:.6px}
  .title-light{font-weight:300;color:var(--muted);line-height:1.15}
  .rule{width:44px;height:2px;background:var(--red)}
  .col{position:absolute}
  .band{position:absolute;left:0;right:0;bottom:0;background:var(--red)}

  .s1{left:50px;top:80px}
  .grid{position:absolute;left:38px;top:58px;width:262px;height:370px;display:grid;grid-template-columns:1fr 1fr;grid-template-rows:repeat(5,1fr);gap:3px}
  .grid .wide{grid-column:span 2}
  .bold-list{font-size:6.6px;font-weight:600;line-height:1.45}
  .bold-list p{margin-bottom:6px}

  .cover{left:790px;top:80px}
  .cover .redbox{position:absolute;left:0;top:110px;width:190px;height:210px;background:var(--red);color:#fff;font-weight:300;font-size:11px;line-height:1.4;padding:34px 24px}
  .badge{position:absolute;top:410px;width:22px;height:22px;border-radius:50%;background:#cfd2d8}

  .s2{left:260px;top:660px}
  .table{font-size:6.3px;color:#fff;line-height:1.55}
  .table .row{display:flex;justify-content:space-between}
  .table .head{font-weight:600;font-size:6.8px}
  .table .gap{margin-top:5px}
  .table .fade{opacity:.85}

  .s3{left:50px;top:1240px}
  .s4{left:620px;top:1240px}
  .small .body{font-size:5.6px}
  .small .h-red{font-size:6px}
  .steps p{margin-bottom:9px}

  .s5{left:50px;top:1720px}
  .prod{position:absolute;top:120px;width:112px}
  .prod .photo{position:relative;height:96px;margin-bottom:12px}
  .prod .body{font-size:6.2px}

  .back{left:790px;top:1720px}
  .contact{position:absolute;right:200px;top:186px;text-align:right;font-size:7px;line-height:1.5}
  .contact strong{font-weight:600}
  .company{position:absolute;left:140px;top:330px;display:flex;align-items:center;gap:8px;color:#fff}
  .company .mark{width:30px;height:24px;border:1.5px solid #fff}
  .company .name{font-size:9px;font-weight:600;line-height:1.2}
  .company .name span{display:block;font-weight:400;font-size:6px}
  .address{position:absolute;left:140px;top:372px;color:#fff;font-size:6px;line-height:1.7}
</style>
</head>
<body>

<section class="spread s1">
  <div class="page">
    <div class="col" style="left:30px;top:60px;width:270px">
      <p class="h-red">3D printing</p>
      <p class="body">Small elements and complex plastic parts inside sensors, such as strain reliefs, are manufactured using a modern 3D printing process. This offers us advantages. Complex designs are produced without detours and without expensive tools. This saves a lot of time and money. By means of 3D printing, special thermometers can be manufactured as a modular system according to customer specifications.</p>
      <p class="h-red" style="margin-top:20px">Inhomogeneity Scanner</p>
      <p class="body">The inhomogeneities of the Vortilon thermocouples are examined with the help of an inhomogeneity scanner. A mobile heat source tests the entire thermal material of the measuring point for local inhomogeneities. The inhomogeneity scanner is a proprietary development of the Brondtweil company.</p>
      <p class="body" style="margin-top:20px;font-size:7.6px;color:#555">The thermocouples of the Vortilon manufacture can be improved substantially by:</p>
      <div class="bold-list" style="margin-top:20px">
        <p>Realistic consideration of the measurement uncertainties</p>
        <p>Optimizing the thermal treatment</p>
        <p>Improvement of quality and manufacturing processes</p>
      </div>
    </div>
  </div>
  <div class="page">
    <span class="brand top">vortilon</span>
    <div class="grid">
      <div class="ph-red" role="img" aria-label="Thermometer handle with red cable"></div>
      <div class="ph-lab" role="img" aria-label="Technician at a microscope"></div>
      <div class="ph-lab" role="img" aria-label="Technician at a lathe"></div>
      <div class="ph-dark" role="img" aria-label="Control panel of a calibration furnace"></div>
      <div class="wide ph-blue" role="img" aria-label="3D printer producing a red part"></div>
      <div class="ph-lab" role="img" aria-label="Welding of a fine sensor wire"></div>
      <div class="ph-warm" role="img" aria-label="Probe in a workshop"></div>
      <div class="ph-lab" role="img" aria-label="Laboratory bench"></div>
      <div class="ph-copper" role="img" aria-label="Copper wire spools"></div>
    </div>
  </div>
</section>

<section class="single cover">
  <div class="page">
    <span class="brand large">vortilon</span>
    <div class="photo ph-lab" style="left:90px;top:150px;width:230px;height:230px" role="img" aria-label="Precision thermometer with red handle in a clamp"></div>
    <div class="redbox">Precision thermometers<br>Resistance thermometers<br>and thermocouples</div>
    <div class="badge" style="left:30px"></div>
    <div class="badge" style="left:58px;border-radius:3px;width:40px"></div>
    <span class="url" style="left:30px">www.vortilon.de</span>
  </div>
</section>

<section class="spread s2">
  <div class="page">
    <div class="col" style="left:40px;top:80px;width:260px">
      <h2 class="title-light" style="font-size:17px">Precision thermometers<br>Resistance thermometers<br>and thermocouples</h2>
      <div class="rule" style="margin:20px 0 24px"></div>
      <p class="body" style="font-size:8px;line-height:1.6;text-align:left">Vortilon precision thermometers are used for precise temperature measurements or as calibration standards. Over many years they have been optimized in the manufacture for precise measurement. The different Vortilon thermometers can be used in a temperature range from -200 C to 1200 C. The resistance thermometers are a robust alternative to the very sensitive ITS-90 standard thermometers. Vortilon thermocouples are made of platinum and can be manufactured with or without stainless steel reference junction.</p>
    </div>
    <span class="url" style="left:40px">www.vortilon.de</span>
  </div>
  <div class="page">
    <span class="brand top">vortilon</span>
    <div class="band" style="top:170px"></div>
    <div class="photo ph-copper" style="left:38px;top:52px;width:264px;height:180px" role="img" aria-label="Thermocouple wire spools and cables on a lab bench"></div>
    <div class="col table" style="left:38px;top:250px;width:120px">
      <p class="head">Type R / Type S<br>Precision Thermocouple</p>
      <p class="gap fade">temperature range 0 C to 1200 C small measurement uncertainties with NAKRA calibration certificate</p>
      <p class="gap">Fixed point calibration</p>
      <div class="row gap"><span>0,01C</span><span>0,2 K</span></div>
      <div class="row"><span>419,527 C</span><span>0,5 K</span></div>
      <div class="row"><span>660,323 C</span><span>0,5 K</span></div>
      <div class="row"><span>961,78 C</span><span>0,6 K</span></div>
      <p class="gap">Comparison calibration</p>
      <div class="row gap"><span>0 C bis 962 C</span><span>0,8 K</span></div>
      <div class="row"><span>&gt;962 C bis 1200C</span><span>1,5 K</span></div>
    </div>
    <div class="col table" style="left:180px;top:250px;width:124px">
      <p class="head">Series HT-40</p>
      <p class="fade">High Temperature Precision thermometer temperature range -100 C to 660 C</p>
      <p class="gap fade">small measurement uncertainties: 6 mK and 25 mK</p>
      <p class="head" style="margin-top:14px">Series IR-24</p>
      <p class="fade">Industrial reference thermometer temperature range -100 C to 600 C</p>
      <p class="gap fade">The temperature sensor with a diameter of 4mm and a small handle enables use in small spaces, e.g. for dry block calibrators.</p>
    </div>
  </div>
</section>

<section class="spread small s3">
  <div class="page">
    <div class="col" style="left:28px;top:70px;width:210px">
      <h2 class="title-light" style="font-size:15px">Technology</h2>
      <div class="rule" style="margin:14px 0 18px;width:34px"></div>
      <p class="body" style="font-size:6.6px;text-align:left">Our thermometers were designed from scratch; the development time took over four years. All components used have been carefully selected and coordinated. Of particular importance is the developed handle, which acts as a technology carrier. Due to its modular design, all thermometers can be combined in any way.</p>
    </div>
    <span class="url" style="left:28px;font-size:5.5px">www.vortilon.de</span>
  </div>
  <div class="page">
    <span class="brand top" style="font-size:9px">vortilon</span>
    <div class="photo ph-lab" style="left:28px;top:60px;width:96px;height:66px" role="img" aria-label="Thermometer handle on a bench"></div>
    <div class="photo ph-red" style="left:138px;top:60px;width:96px;height:66px" role="img" aria-label="Sensor tubes in a red rack"></div>
    <div class="col" style="left:28px;top:140px;width:96px">
      <p class="h-red">The handle as technology carrier</p>
      <p class="body">Our handle is built as a modular unit. It holds the electronics, the strain relief and the cable entry, and it keeps the cold junction stable during every measurement.</p>
    </div>
    <div class="col" style="left:138px;top:140px;width:96px">
      <p class="h-red">Temperature detectors</p>
      <p class="body">For the detectors we use only selected platinum elements. Each one is checked, aged and sorted before it is mounted into a sheath.</p>
      <p class="body" style="margin-top:6px">• Stable long-term drift<br>• Fast response time<br>• Robust sheath design</p>
    </div>
  </div>
</section>

<section class="spread small s4">
  <div class="page">
    <div class="photo ph-lab" style="left:0;top:0;width:265px;height:86px" role="img" aria-label="Workshop with copper spools and red cabinets"></div>
    <div class="col" style="left:28px;top:104px;width:210px">
      <h2 class="title-light" style="font-size:14px">Precision thermometers<br>handmade</h2>
      <div class="rule" style="margin:12px 0 14px;width:34px"></div>
      <p class="body" style="font-size:6.2px;text-align:left">In the Vortilon manufacture of Brondtweil the precision thermometers are manufactured by careful manual work in Kassel/Germany. In addition to the construction of the actual thermometers, the focus is on the development of our own tools and production processes. For design, production and final calibration, no external suppliers are required. This independence from raw materials ensures the high quality of the thermometers.</p>
    </div>
    <div class="photo ph-dark" style="left:28px;top:300px;width:140px;height:40px" role="img" aria-label="Black thermometer handle with red ring"></div>
  </div>
  <div class="page">
    <span class="brand top" style="font-size:9px">vortilon</span>
    <div class="col steps" style="left:28px;top:62px;width:210px">
      <p><span class="h-red">Mechanical production</span><br><span class="body">Turned and milled parts are produced in-house for quick development steps.</span></p>
      <p><span class="h-red">Noble metal welding process</span><br><span class="body">Fine platinum wires are joined under protective gas to keep the junction pure and stable.</span></p>
      <p><span class="h-red">Laser Welding</span><br><span class="body">Sheaths and housings are sealed by laser, giving tight seams with minimal heat input.</span></p>
      <p><span class="h-red">Thermal treatment of thermal material</span><br><span class="body">Wires are annealed in our furnaces to reduce drift and remove inner stress.</span></p>
      <p><span class="h-red">Annealing of resistance thermometers</span><br><span class="body">Each finished sensor is aged over many cycles before the final calibration.</span></p>
    </div>
  </div>
</section>

<section class="spread s5">
  <div class="page">
    <div class="prod" style="left:30px">
      <div class="photo ph-gold" role="img" aria-label="Spool of thermometer wire"></div>
      <p class="h-red">Thermometer wire</p>
      <p class="body">As thermometer wire at the measuring resistors and in the capillaries we use noble metals and no commercial coated wires. Depending on the temperature range, these are pure silver or platinum. In this way we reduce thermoelectric effects in the thermometer.</p>
    </div>
    <div class="prod" style="left:160px">
      <div class="photo ph-red" role="img" aria-label="Protection tubes in a rack"></div>
      <p class="h-red">Protection tubes</p>
      <p class="body">Protection tubes are selected with regard to thermal stress and the nature of the atmosphere. In order to protect the temperature sensor optimally against mechanical and chemical influences, protection tubes made of pure ceramics, noble metals, high-temperature alloys or sapphire are used, depending on the application.</p>
    </div>
    <span class="url" style="left:30px">www.vortilon.de</span>
  </div>
  <div class="page">
    <span class="brand top">vortilon</span>
    <div class="prod" style="left:38px">
      <div class="photo ph-copper" role="img" aria-label="Connection cable spools"></div>
      <p class="h-red">Connection cables</p>
      <p class="body">Connection cables for thermocouples and resistance thermometers are assembled by hand. We use copper strands made of a low-stress copper alloy which was cast especially for our thermometers. A reinforced textile sheath made of heat-treated fibreglass protective tube, which is resistant to high temperatures, serves as an insulating sheath. This protects the individual strands from mechanical stress, high temperatures and organic solvents.</p>
    </div>
    <div class="prod" style="left:170px">
      <div class="photo ph-dark" role="img" aria-label="Thermometer in a foam-lined carrying case"></div>
      <p class="h-red">High quality carrying case</p>
      <p class="body">All Vortilon thermometers are delivered in a high-quality wooden carrying case. Due to the robust wooden case with the adapted foam inlay the sensitive thermometers are well protected during transport and storage. Alternatively and at a lower price, the thermometer can also be delivered without the case in a cardboard box.</p>
    </div>
    <div class="photo ph-red" style="left:185px;top:395px;width:100px;height:30px" role="img" aria-label="Closed carrying case"></div>
  </div>
</section>

<section class="single back">
  <div class="page">
    <span class="brand large" style="right:auto;left:34px">vortilon</span>
    <div class="band" style="top:255px"></div>
    <div class="photo ph-person" style="left:150px;top:95px;width:170px;height:215px" role="img" aria-label="Portrait of the contact person"></div>
    <div class="contact">
      <strong>Contact Person</strong><br>
      Marta Lindqvist<br>
      m.lindqvist@brondtweil.com
    </div>
    <div class="company">
      <div class="mark"></div>
      <p class="name">Brondtweil<span>Messen mit Ruhe</span></p>
    </div>
    <p class="address">
      Brondtweil Kalibrier- und Messtechnik GmbH<br>
      Talweg 8 · 34117 Kassel<br>
      Tel.: +49 561 200 400-0<br>
      Mail: info@brondtweil.com
    </p>
  </div>
</section>

</body>
</html>
```